Quorvane needs a new design we have an updated logo and want a high qualitative high end feel

feel and aesthetic should be high qualitative like the packaging in a zuvi or the qualatative weight/feel of an zuvi design. modern, elegant bold.probably just the quorvane logo on the backone vesion could be blue background white letter ... open to ideas
Target Market(s)
legal, insurance , medical, finance rho 740
Industry/Entity Type
Information Technology
Font styles to use
Serif

```html
<!DOCTYPE html>
<html lang="en">
<head>
<meta charset="utf-8">
<title>Quorvane — Business Card</title>
<link href="https://fonts.googleapis.com/css2?family=Montserrat:wght@400;500;700&family=Poppins:wght@500&display=swap" rel="stylesheet">
<style>
  :root {
    --bg: #5ccbe9;
    --bg-deep: #3db6e0;
    --navy: #1c2b3d;
    --navy-dark: #0e1a29;
    --navy-soft: #2a3f57;
    --ink: #17283a;
    --paper: #ffffff;
    --muted: #d9e2ec;
  }
  html, body {
    margin: 0;
    width: 1200px;
    height: 1051px;
    overflow: hidden;
  }
  body {
    background: radial-gradient(circle at 35% 50%, var(--bg) 0%, var(--bg) 55%, var(--bg-deep) 100%);
    font-family: "Montserrat", Arial, sans-serif;
    position: relative;
  }
  .card {
    position: absolute;
    left: 320px;
    width: 560px;
    height: 320px;
    box-shadow: 0 18px 34px rgba(10, 40, 70, 0.22);
    overflow: hidden;
  }
  /* Front */
  .card-front {
    top: 120px;
    background: var(--paper);
  }
  .card-front .top-band {
    position: absolute;
    top: 0; left: 0; right: 0;
    height: 12px;
    background: linear-gradient(90deg, var(--navy-soft), var(--navy-dark));
  }
  .brand {
    position: absolute;
    top: 118px;
    left: 0; right: 0;
    display: flex;
    justify-content: center;
    align-items: center;
    gap: 12px;
  }
  .brand-dot {
    width: 14px;
    height: 14px;
    border-radius: 50%;
    background: var(--ink);
  }
  .brand-name {
    font-family: "Poppins", Arial, sans-serif;
    font-weight: 500;
    font-size: 58px;
    line-height: 1;
    color: var(--ink);
    letter-spacing: 1px;
  }
  .website {
    position: absolute;
    bottom: 52px;
    left: 0; right: 0;
    text-align: center;
    font-size: 14px;
    letter-spacing: 5px;
    color: var(--ink);
  }
  /* Back */
  .card-back {
    top: 560px;
    background: var(--navy);
    color: var(--paper);
  }
  .name-ribbon {
    position: absolute;
    top: 96px;
    left: 0;
    width: 300px;
    height: 58px;
    background: var(--navy-dark);
    clip-path: polygon(0 0, 84% 0, 100% 60%, 100% 100%, 0 100%);
  }
  .person-name {
    position: absolute;
    top: 113px;
    left: 62px;
    font-weight: 700;
    font-size: 19px;
    line-height: 24px;
    letter-spacing: 0.3px;
    margin: 0;
  }
  .contact-list {
    position: absolute;
    top: 186px;
    left: 62px;
    margin: 0;
    padding: 0;
    list-style: none;
  }
  .contact-list li {
    display: flex;
    align-items: center;
    gap: 16px;
    height: 30px;
    font-size: 14px;
    color: var(--muted);
  }
  .contact-list svg {
    width: 14px;
    height: 14px;
    fill: var(--paper);
    flex: none;
  }
  .accent-bar {
    position: absolute;
    bottom: 0;
    height: 8px;
    background: var(--navy-soft);
  }
  .accent-bar.wide { left: 200px; width: 150px; }
  .accent-bar.short { right: 40px; width: 70px; background: var(--navy-dark); bottom: 14px; }
</style>
</head>
<body>

<section class="card card-front">
  <div class="top-band"></div>
  <div class="brand">
    <span class="brand-dot"></span>
    <span class="brand-name">quorvane</span>
  </div>
  <div class="website">www.quorvane.com</div>
</section>

<section class="card card-back">
  <div class="name-ribbon"></div>
  <h1 class="person-name">YOUR NAME HERE</h1>
  <ul class="contact-list">
    <li>
      <svg viewBox="0 0 24 24" aria-hidden="true"><path d="M6.6 10.8a15.1 15.1 0 0 0 6.6 6.6l2.2-2.2a1 1 0 0 1 1-.25 11.4 11.4 0 0 0 3.6.6 1 1 0 0 1 1 1V20a1 1 0 0 1-1 1A17 17 0 0 1 3 4a1 1 0 0 1 1-1h3.5a1 1 0 0 1 1 1c0 1.25.2 2.45.6 3.6a1 1 0 0 1-.25 1z"/></svg>
      Your Contact no.
    </li>
    <li>
      <svg viewBox="0 0 24 24" aria-hidden="true"><path d="M2 5h20v14H2z M3.5 6.5 12 13l8.5-6.5" fill="var(--paper)" stroke="var(--navy)" stroke-width="1.4"/></svg>
      youremailid@quorvane.com
    </li>
    <li>
      <svg viewBox="0 0 24 24" aria-hidden="true"><path d="M12 2a7 7 0 0 0-7 7c0 5.2 7 13 7 13s7-7.8 7-13a7 7 0 0 0-7-7zm0 9.5A2.5 2.5 0 1 1 12 6.5a2.5 2.5 0 0 1 0 5z"/></svg>
      Your Address here
    </li>
  </ul>
  <div class="accent-bar wide"></div>
  <div class="accent-bar short"></div>
</section>

</body>
</html>
```